Custom Header Designs - Automotive Parts - Alternator & Starter

We need 8 Header/Hero designs that will be used on our website. We are a company based in Montreal Canada and we re-manufacture Alternators and Starters for all types of vehicles. We offer a premium product and we are looking for premium designs that reflect the look of our packaging and the look of our website. Essentially we specialize in the sale and manufacture of two specific parts that go on all types of vehicles, Alternators and Starters. All text on these designs need to be editable as we will need to translate them to French once we get the source files.
Here are some websites of our competitors so you can draw some inspiration and see what our industry/business is all about:
https://www.qelvorparts.com/
https://www.zentrihaul.com/
Article that describes a remanufactured product, https://www.wombrixo.com/articles/starters-and-alternators-reman-vs-new.html
Our packaging is modern, sleek and professional. Our website is a B2B E-Commerce Site as well as an info site to promote our products. It is clean and minimal but we want the header/hero designs to help it stand out. Our main colors are blue and gray (as seen in our logo), but you can use whatever you like to compliment these colors.
Our packaging design was done on PixelTroupe, here is the link to that project so that you can see the packaging look and use any of the info that is from that project.
https://jobs.pixeltroupe.ca/job/5829463
The 8 Header/Hero designs will be used in the following areas, I have included a brief description of what we are looking for:
1 - Homepage Header/Hero image - This will be the homepage hero image therefore it should summarize the info described below. We offer premium quality re-manufactured alternators and starters. We are a wholesaler/distributor that services major auto-part stores with these quality products.
2 - General Product Header/Hero image - This image will be used as a header where the customer can learn general info about our products and any custom work we can do. This page will have a section where you can click to learn more about our individual product lines (links to product specific pages mentioned below) and a description of the custom work we can perform. We offer a two year manufacturers warranty.
3 - Alternator Product Header/Hero image - This image will be used to showcase our Alternator Product Line. Its purpose is to promote and advertise our premium re-manufactured alternators. This page will provide detailed info about our alternator re-manufacturing process and describe why our alternators are great.
4 - Starter Product Header/Hero image - This image will be used to showcase our Starter Product Line. Its purpose is to promote and advertise our premium re-manufactured starters. This page will provide detailed info about our starter re-manufacturing process and describe why our starters are great.
5 - General Header/Hero Image - This image will be used in most of our standard pages like our terms and conditions, privacy policy, warranty policy, our company page, etc. It needs to relate to the industry but be general enough so that we could use it in multiple areas
6 - Online Ordering Header image - This image will be used in our B2B area to introduce our customers to the Online Ordering system, its purpose is to advertise and explain some of the features of the Online Ordering system.
7 - B/O Re-Manufacture & Return Header Image - This image will be used in our B2B area to explain and advertise to our customers how our Backorder/R&R process works on our website. Essentially if we do not have the remanufactured part in stock but we have the core you could put the product on Backorder and we will remanufacture it in a few hours. If for any reason (rare vehicle, old vehicle, etc.) we do not have the core we will R&R (Remanufacture and Return) the customers core for them.
8 - Bulk Ordering Form Header Image - This image will be used in our B2B area to explain and advertise to our customers how our Bulk Ordering Form works on our website.
These hero/header images will be going on a Plankly/TillNest website and I am suggesting these images have a size of 1600 x 500, but we will take any other suggestions from the designers as you are the experts.
I have included a zip file that includes images of various elements that will help you in the design process.
Target Market(s)
Educate consumers about our products and attract auto supply chains to become distributors of our products.
Industry/Entity Type
Automotive Part

```html
<!DOCTYPE html>
<html lang="en">
<head>
<meta charset="utf-8">
<title>Kelvane – Premium Re-Manufactured Alternators &amp; Starters</title>
<link href="https://fonts.googleapis.com/css2?family=Montserrat:ital,wght@0,500;1,800&family=Exo+2:ital,wght@1,900&family=Roboto:wght@400;500&display=swap" rel="stylesheet">
<style>
  :root {
    --brand-blue: #1d3a9a;
    --link-blue: #2b3fa8;
    --hero-blue: #17338f;
    --hero-deep: #10256e;
    --accent-yellow: #f5d936;
    --cta-red: #c8101e;
    --topbar-bg: #f4f4f4;
    --nav-text: #555555;
    --muted: #777777;
    --white: #ffffff;
  }
  * { box-sizing: border-box; margin: 0; padding: 0; }
  html, body { width: 1200px; height: 520px; overflow: hidden; background: var(--white); }
  .page { position: relative; width: 1200px; height: 520px; font-family: "Roboto", Arial, sans-serif; }

  .topbar { position: absolute; left: 0; top: 0; width: 1200px; height: 25px; background: var(--topbar-bg); font-size: 10px; }
  .topbar span { position: absolute; top: 7px; white-space: nowrap; }
  .topbar .consult { left: 198px; color: var(--link-blue); }
  .topbar .call { left: 550px; color: var(--muted); }
  .topbar .call b { color: #333; font-weight: 500; }
  .topbar .divider { left: 677px; color: #aaa; }
  .topbar .map { left: 692px; color: var(--link-blue); }
  .topbar .dashboard { left: 808px; top: 9px; font-size: 7.5px; color: var(--link-blue); letter-spacing: .2px; }
  .topbar .lang { left: 932px; top: 8px; font-size: 7.5px; color: #444; }
  .topbar .lang i { display: inline-block; width: 12px; height: 8px; background: #c8102e; margin-right: 3px; vertical-align: -1px; }

  .navbar { position: absolute; left: 0; top: 25px; width: 1200px; height: 72px; background: var(--white); }
  .brand { position: absolute; left: 207px; top: 20px; display: flex; align-items: center; gap: 8px; }
  .brand-dot { width: 30px; height: 30px; border-radius: 50%; background: var(--brand-blue); }
  .brand-name { font-family: "Montserrat", Arial, sans-serif; font-weight: 500; font-size: 24px; color: var(--brand-blue); }
  .menu a { position: absolute; top: 26px; font-size: 10.6px; color: var(--nav-text); text-decoration: none; white-space: nowrap; }
  .menu a.account { color: var(--link-blue); border-bottom: 1px solid var(--link-blue); padding-bottom: 2px; }
  .cart { position: absolute; left: 973px; top: 30px; }
  .cart-count { position: absolute; left: 990px; top: 22px; width: 13px; height: 13px; border-radius: 50%; background: #8fd3f0; color: #234; font-size: 7px; text-align: center; line-height: 13px; }

  .hero { position: absolute; left: 0; top: 97px; width: 1200px; height: 423px; overflow: hidden; }
  .hero-backdrop { position: absolute; inset: 0; background: radial-gradient(ellipse at 40% 50%, var(--hero-blue), var(--hero-deep)); }
  .tagline { position: absolute; left: 167px; top: 61px; font-family: "Montserrat", Arial, sans-serif; font-style: italic; font-weight: 800; font-size: 21px; line-height: 27px; color: var(--accent-yellow); text-shadow: 0 2px 4px rgba(0,0,0,.3); }
  .headline { position: absolute; left: 158px; top: 113px; font-family: "Exo 2", Arial, sans-serif; font-style: italic; font-weight: 900; font-size: 38px; line-height: 40px; color: var(--white); text-shadow: 0 3px 6px rgba(0,0,0,.35); }
  .order-button { position: absolute; left: 158px; top: 218px; width: 173px; height: 45px; background: var(--cta-red); border: 2px solid var(--white); border-radius: 3px; color: var(--white); font-family: "Montserrat", Arial, sans-serif; font-weight: 500; font-size: 16px; text-align: center; line-height: 41px; letter-spacing: .3px; }
  .product-art { position: absolute; left: 0; top: 0; }
</style>
</head>
<body>
<div class="page">
  <div class="topbar">
    <span class="consult">Book a Sales Consultation →</span>
    <span class="call">Call us now: <b>555.210.4478</b></span>
    <span class="divider">|</span>
    <span class="map">Find us on the map →</span>
    <span class="dashboard">MY KELVANE DASHBOARD</span>
    <span class="lang"><i></i>English (English)</span>
  </div>

  <header class="navbar">
    <div class="brand"><span class="brand-dot"></span><span class="brand-name">Kelvane</span></div>
    <nav class="menu">
      <a style="left:406px">Home</a>
      <a style="left:452px">Products</a>
      <a style="left:511px">Our Company</a>
      <a style="left:594px">Customer Resources</a>
      <a style="left:712px">Contact Us</a>
      <a style="left:782px">Online Ordering</a>
      <a class="account" style="left:874px">Hello, administrator</a>
    </nav>
    <svg class="cart" width="16" height="16" viewBox="0 0 16 16" fill="none" stroke="#333" stroke-width="1.2">
      <rect x="2" y="6" width="12" height="9" rx="1"/>
      <path d="M5 6 V4 a3 3 0 0 1 6 0 V6"/>
    </svg>
    <span class="cart-count">2</span>
  </header>

  <section class="hero">
    <div class="hero-backdrop" role="img" aria-label="Blurred engine bay photograph tinted deep blue"></div>
    <svg class="product-art" width="1200" height="423" viewBox="0 0 1200 423">
      <circle cx="653" cy="175" r="143" fill="#ffffff"/>
      <circle cx="653" cy="175" r="139" fill="var(--accent-yellow)"/>
      <circle cx="923" cy="248" r="128" fill="#ffffff"/>
      <circle cx="923" cy="248" r="124" fill="var(--accent-yellow)"/>
      <g role="img" aria-label="Photo of a silver re-manufactured alternator">
        <defs>
          <linearGradient id="metal" x1="0" y1="0" x2="1" y2="1">
            <stop offset="0" stop-color="#e4e6ea"/>
            <stop offset="1" stop-color="#9ca2ab"/>
          </linearGradient>
        </defs>
        <path d="M470 90 L600 65 L700 110 L740 200 L700 300 L560 340 L450 300 L440 190 Z" fill="url(#metal)"/>
      </g>
      <g role="img" aria-label="Photo of a silver re-manufactured starter motor">
        <path d="M760 175 L860 175 L950 178 L1000 195 L1030 250 L1010 330 L940 362 L860 350 L800 320 L755 290 Z" fill="url(#metal)"/>
      </g>
    </svg>
    <div class="tagline">PREMIUM QUALITY<br>RE-MANUFACTURED</div>
    <div class="headline">Alternators<br>&amp; Starters</div>
    <div class="order-button">ORDER NOW</div>
  </section>
</div>
</body>
</html>
```